Billboard for personal injury chiropractors office

We are a personal injury chiropractor clinic.
I need a Billboard with the company name as the dominating factor. Also a smaller picture or 2 of something creative, like a car accident or an arm in a cast off to the sides.
We Like something Clean and Simple and Eye Catching. Please make the picture Small and Off To The Side. The MAIN FOCUS areas are the… name Pell Chiropractic Clinic
At the top CAR ACCIDENT INJURY?
AND at the bottom our number 581-47-TORSO.
Dr.Marla T. Pell in bold somewhere with the word chiropractor under the doctors name in a text.

Im open to red lettering on white backgrounds, red on yellow backgrounds and I'm also open to reds blues white and yellow. I'd prefer yellow if used be across the bottom.

I am uploading a very rough draft of what we are after along with a screenshot of the tv commercial showing the yellow

DO NOT USE THE LOGO ON THE COMMERCIAL. I JUST WANT THE NAME TYPED LIKE ON SAMPLE BILLBOARD.

Industry/Entity Type

Chiropractic

Colors
0054AA
0677BA
7BADD7
CADEEF
E8F1F8
FFF300
FFF600
FEFA6F
FFFEC7
FFFEE8
EB3D1F
EC4F4E
F09395
F8D3D4
FCEDEE

Requirements
Must have
• Eye catching ,bold

```html
<!DOCTYPE html>
<html lang="en">
<head>
<meta charset="utf-8">
<title>Pell Chiropractic Clinic – Billboard</title>
<link rel="stylesheet" href="https://fonts.googleapis.com/css2?family=Bebas+Neue&family=Montserrat:wght@700;800;900&display=swap">
<style>
  :root {
    --page: #4a4a4a;
    --white: #ffffff;
    --red: #d3202a;
    --navy: #263a73;
    --yellow: #fff300;
    --yellow-shade: #8f8a12;
  }
  * { margin: 0; padding: 0; box-sizing: border-box; }
  html, body { width: 989px; height: 1200px; overflow: hidden; }
  body {
    background: var(--page);
    display: flex;
    align-items: center;
    justify-content: center;
  }
  .billboard {
    position: relative;
    width: 940px;
    height: 274px;
    background: var(--white);
    overflow: hidden;
  }
  .band { position: absolute; left: 0; right: 0; }
  .band-name { top: 73px; height: 75px; background: var(--navy); }
  .band-doctor { top: 148px; height: 36px; background: var(--white); }
  .band-phone {
    top: 184px; height: 90px;
    background: linear-gradient(90deg, var(--yellow) 0%, var(--yellow) 78%, var(--yellow-shade) 100%);
  }
  .headline {
    position: absolute;
    left: 0; right: 0; top: 4px;
    text-align: center;
    white-space: nowrap;
    font-family: "Montserrat", sans-serif;
    font-weight: 900;
    font-size: 64px;
    line-height: 66px;
    color: var(--red);
  }
  .clinic-name {
    position: absolute;
    left: 160px; width: 640px; top: 80px;
    font-family: "Bebas Neue", sans-serif;
    font-weight: 400;
    font-size: 68px;
    line-height: 62px;
    color: var(--white);
    text-align: center;
    white-space: nowrap;
    transform: scaleY(1.15);
    transform-origin: center top;
  }
  .doctor {
    position: absolute;
    left: 200px; width: 600px; top: 149px;
    font-family: "Montserrat", sans-serif;
    font-weight: 800;
    font-size: 29px;
    line-height: 34px;
    letter-spacing: 0.5px;
    color: var(--navy);
    text-align: center;
    white-space: nowrap;
  }
  .doctor .role { color: var(--red); }
  .phone {
    position: absolute;
    left: 285px; top: 190px;
    display: flex;
    align-items: center;
    gap: 10px;
    white-space: nowrap;
  }
  .phone-icon { width: 70px; height: 70px; flex: none; }
  .phone-number {
    font-family: "Bebas Neue", sans-serif;
    font-size: 90px;
    line-height: 80px;
    color: var(--red);
    transform: scaleY(1.08);
    transform-origin: left center;
  }
  .art { position: absolute; top: 0; left: 0; width: 940px; height: 274px; }
</style>
</head>
<body>
  <div class="billboard">
    <div class="band band-name"></div>
    <div class="band band-doctor"></div>
    <div class="band band-phone"></div>

    <svg class="art" viewBox="0 0 940 274">
      <defs>
        <linearGradient id="armPhoto" x1="0" y1="0" x2="1" y2="1">
          <stop offset="0" stop-color="#1c1f26"/>
          <stop offset="0.55" stop-color="#3a3a40"/>
          <stop offset="1" stop-color="#a88a6a"/>
        </linearGradient>
        <linearGradient id="carPhoto" x1="0" y1="0" x2="1" y2="1">
          <stop offset="0" stop-color="#d23a3f"/>
          <stop offset="0.5" stop-color="#a3121b"/>
          <stop offset="1" stop-color="#5a1014"/>
        </linearGradient>
      </defs>
      <polygon class="accent-corner" points="0,60 30,46 96,104 0,190" fill="#e31e24"/>
      <path class="photo-arm" role="img" aria-label="Photo of a person with a bandaged arm in a sling"
            d="M0,88 L72,88 L300,226 Q318,240 312,260 L308,274 L0,274 Z" fill="url(#armPhoto)"/>
      <path class="photo-car" role="img" aria-label="Photo of the crumpled front of a red car after a crash"
            d="M830,92 Q900,80 940,86 L940,274 L840,274 Q808,240 812,200 Q818,120 830,92 Z" fill="url(#carPhoto)"/>
    </svg>

    <h1 class="headline">CAR ACCIDENT INJURY?</h1>
    <h2 class="clinic-name">PELL CHIROPRACTIC CLINIC</h2>
    <p class="doctor">Dr.Marla T. Pell - <span class="role">Chiropractor</span></p>

    <div class="phone">
      <svg class="phone-icon" viewBox="0 0 70 70" aria-hidden="true">
        <circle cx="35" cy="35" r="34" fill="#d3202a"/>
        <circle cx="35" cy="35" r="29" fill="none" stroke="#fff300" stroke-width="2"/>
        <path d="M24 20 q4 -2 6 2 l3 6 q1 3 -2 5 l-2 1 q3 7 9 11 l2 -2 q2 -2 5 -1 l6 3 q3 2 1 6 l-2 3 q-3 3 -9 1 q-14 -6 -20 -20 q-2 -7 1 -10 z" fill="#fff300"/>
      </svg>
      <span class="phone-number">581-47-TORSO</span>
    </div>
  </div>
</body>
</html>
```